martial arts school needs a flyer to attract new starters in wing chun kung fu

we need a flyer design to be sent out in the local community to attract new customers to our martial arts school. we intend to run introduction classes for begineers. the design should be attractive to new starters looking to get fit - learn a martial art - make new friends - improve self confidence.
also the flyer should say "free class with this flyer" . we also need big poster to put up around the local area

the following dress should be on the design Aire Valley Martial ArtsGround FloorThe MillGreengage RoadKeighleyBD21 5LH Added Sunday, April 5, 2015

contact telephone number on the design ; 079 64820 557 Added Sunday, April 5, 2015

• it must say - wing chun kung fu classes - introduction classes -

```html
<!DOCTYPE html>
<html lang="en">
<head>
<meta charset="utf-8">
<title>Wing Chun Kung Fu Classes – Flyer</title>
<link rel="stylesheet" href="https://fonts.googleapis.com/css2?family=Anton&family=Oswald:wght@700&family=Archivo+Black&family=Arimo:wght@400;700&display=swap">
<style>
  :root {
    --red: #e8202a;
    --navy: #14223f;
    --ink: #111111;
    --blue-band: #1a5aa6;
    --yellow: #fff200;
    --paper: #ffffff;
    --photo-light: #eef1f6;
    --photo-mid: #cfd6e2;
    --badge-grey: #cfcfcf;
    --badge-ink: #2b2b2b;
  }
  * { margin: 0; padding: 0; box-sizing: border-box; }
  html, body { width: 846px; height: 1200px; overflow: hidden; background: var(--paper); }
  .flyer {
    position: relative;
    width: 846px;
    height: 1200px;
    background: linear-gradient(90deg, var(--photo-light) 0%, var(--paper) 55%);
    font-family: "Arimo", Arial, sans-serif;
    color: var(--ink);
    overflow: hidden;
  }
  .student-photo {
    position: absolute;
    left: 0; top: 0;
    width: 400px; height: 1000px;
    background: linear-gradient(180deg, var(--photo-light) 0%, var(--photo-mid) 100%);
  }
  .headline {
    position: absolute;
    right: 30px; top: 58px;
    text-align: right;
  }
  .headline__main {
    font-family: "Anton", Impact, sans-serif;
    font-size: 122px;
    line-height: 1;
    color: var(--red);
    letter-spacing: 1px;
  }
  .headline__sub {
    font-family: "Oswald", "Arial Narrow", sans-serif;
    font-weight: 700;
    font-size: 50px;
    line-height: 1;
    color: var(--navy);
    letter-spacing: 9px;
    margin-top: 6px;
  }
  .headline-rule {
    position: absolute;
    left: 262px; right: 0; top: 252px;
    height: 2px;
    background: var(--navy);
  }
  .intro {
    position: absolute;
    left: 308px; top: 258px;
    font-weight: 700;
    font-size: 33px;
    color: var(--ink);
  }
  .school-mark {
    position: absolute;
    left: 430px; top: 320px;
    width: 260px;
    text-align: center;
  }
  .school-mark__circle {
    width: 170px; height: 170px;
    margin: 0 auto 18px;
    border-radius: 50%;
    background: var(--badge-grey);
  }
  .school-mark__name {
    font-weight: 700;
    font-size: 24px;
    line-height: 1.2;
    letter-spacing: 2px;
    color: var(--badge-ink);
    text-transform: uppercase;
  }
  .benefits {
    position: absolute;
    right: 36px; top: 632px;
    list-style: none;
    text-align: right;
    transform: rotate(-2.5deg);
    transform-origin: right top;
  }
  .benefits li {
    font-family: "Archivo Black", "Arial Black", sans-serif;
    color: var(--navy);
    line-height: 60px;
    -webkit-text-stroke: 0;
    text-shadow: 2px 0 var(--paper), -2px 0 var(--paper), 0 2px var(--paper), 0 -2px var(--paper);
  }
  .benefits .b1 { font-size: 44px; }
  .benefits .b2 { font-size: 46px; }
  .benefits .b3 { font-size: 48px; }
  .benefits .b4 { font-size: 49px; }
  .divider {
    position: absolute;
    left: 0; top: 926px;
    width: 846px; height: 8px;
    display: flex;
  }
  .divider__blue { width: 752px; background: var(--blue-band); }
  .divider__gap { width: 10px; background: var(--paper); }
  .divider__navy { flex: 1; background: var(--navy); }
  .contact {
    position: absolute;
    left: 0; top: 934px;
    width: 846px; height: 180px;
    background: var(--paper);
    text-align: center;
  }
  .contact__phone {
    display: flex;
    justify-content: center;
    align-items: center;
    gap: 18px;
    margin-top: 28px;
    margin-left: 130px;
    font-weight: 700;
    font-size: 62px;
    line-height: 1;
  }
  .contact__phone svg { width: 70px; height: 54px; }
  .contact__address {
    margin-top: 18px;
    margin-left: 130px;
    font-size: 26px;
    line-height: 1.25;
  }
  .offer {
    position: absolute;
    left: 20px; right: 20px; top: 1114px;
    height: 74px;
    background: var(--yellow);
    display: flex;
    align-items: center;
    justify-content: center;
    font-weight: 700;
    font-size: 38px;
    color: var(--red);
  }
</style>
</head>
<body>
<main class="flyer">
  <div class="student-photo" role="img" aria-label="Photo of a smiling student in a white martial arts uniform and black belt, arms folded"></div>

  <header class="headline">
    <h1 class="headline__main">WING CHUN</h1>
    <p class="headline__sub">KUNG FU CLASSES</p>
  </header>
  <div class="headline-rule"></div>
  <p class="intro">INTRODUCTION CLASSES</p>

  <div class="school-mark">
    <div class="school-mark__circle"></div>
    <p class="school-mark__name">Brook Hollow<br>Martial Arts</p>
  </div>

  <ul class="benefits">
    <li class="b1">GET FIT</li>
    <li class="b2">MAKE NEW FRIENDS</li>
    <li class="b3">LEARN A MARTIAL ART</li>
    <li class="b4">IMPROVE SELF-CONFIDENCE</li>
  </ul>

  <div class="divider">
    <span class="divider__blue"></span><span class="divider__gap"></span><span class="divider__navy"></span>
  </div>

  <section class="contact">
    <p class="contact__phone">
      <svg viewBox="0 0 70 54" aria-hidden="true">
        <path d="M4 18 C4 6 66 6 66 18 L66 22 L50 22 L50 15 L20 15 L20 22 L4 22 Z" fill="#111"/>
        <path d="M14 26 L56 26 L64 50 L6 50 Z" fill="#111"/>
        <circle cx="35" cy="38" r="7" fill="#fff"/>
      </svg>
      <span>079 64820 557</span>
    </p>
    <p class="contact__address">Brook Hollow Martial Arts Ground Floor<br>The Tannery Spindlewick Road Ashcombe TQ47 9RX</p>
  </section>

  <p class="offer">Bring this flyer in for a FREE WEEK!</p>
</main>
</body>
</html>
```